Business Card

We need a business card designed using one of the attached logo designs (our preference is for the boxes version, but if you think it looks better with the horizontal version we will consider those too). Standard business card dimensions.

Details that need to be included:

Tobias Freel
Morlanex S.L.U
tobias@morlanex.example

Phone numbers:
(UK) +44 771 4052 368
(Spain) +34 681 503 427

Twitter: @Morlanex
Web: http://www.morlanex.example

Tagline (optional, if it doesnt make it look too cluttered):
Automation and configuration management specialists
or
Configuration management specialists

```html
<!DOCTYPE html>
<html lang="en">
<head>
<meta charset="utf-8">
<title>Morlanex Business Card</title>
<link rel="stylesheet" href="https://fonts.googleapis.com/css2?family=Arimo:wght@400;700&display=swap">
<style>
  :root {
    --page-bg: #dcd8d3;
    --card-white: #f1f1f1;
    --wave-light: #33b3e3;
    --wave-deep: #2a8fe0;
    --swoosh: #222222;
    --ink-dark: #232323;
    --ink-light: #ffffff;
    --mark-blue: #2d8fe0;
  }
  * { margin: 0; padding: 0; box-sizing: border-box; }
  html, body {
    width: 1200px; height: 900px; overflow: hidden;
    background: var(--page-bg);
    font-family: "Arimo", Arial, sans-serif;
  }
  .card {
    position: absolute; left: 100px; top: 164px;
    width: 1000px; height: 572px;
    background: var(--card-white);
    overflow: hidden;
    box-shadow: 0 10px 30px rgba(0,0,0,0.18);
  }
  .card-art { position: absolute; inset: 0; width: 100%; height: 100%; }
  .brand {
    position: absolute; left: 60px; top: 58px;
    display: flex; flex-direction: column; align-items: flex-start; gap: 22px;
  }
  .brand-square {
    width: 200px; height: 160px; border-radius: 14px;
    background: var(--mark-blue);
  }
  .brand-name {
    font-weight: 700; font-size: 50px; letter-spacing: 2px;
    color: var(--ink-dark);
  }
  .contact {
    position: absolute; right: 48px; top: 178px;
    text-align: right; color: var(--ink-light);
  }
  .contact-name {
    font-weight: 700; font-size: 40px; margin-bottom: 10px; padding-right: 30px;
  }
  .contact-line {
    display: flex; justify-content: flex-end; align-items: center; gap: 8px;
    font-size: 29px; line-height: 37px;
  }
  .contact-icon { width: 22px; height: 22px; flex: none; }
  .website {
    position: absolute; left: 60px; bottom: 34px;
    font-size: 30px; letter-spacing: 9px; color: var(--ink-light);
  }
</style>
</head>
<body>
  <div class="card">
    <svg class="card-art" viewBox="0 0 1000 572" preserveAspectRatio="none" aria-hidden="true">
      <defs>
        <linearGradient id="waveFill" x1="1" y1="0" x2="0" y2="1">
          <stop offset="0" stop-color="var(--wave-light)"/>
          <stop offset="1" stop-color="var(--wave-deep)"/>
        </linearGradient>
      </defs>
      <path d="M1000,80 C800,70 690,170 600,290 C510,420 360,495 0,505 L0,572 L1000,572 Z" fill="url(#waveFill)"/>
      <path d="M0,462 C220,478 420,450 540,345 C450,445 250,495 0,500 Z" fill="var(--swoosh)"/>
    </svg>

    <div class="brand">
      <div class="brand-square"></div>
      <div class="brand-name">MORLANEX</div>
    </div>

    <div class="contact">
      <div class="contact-name">Tobias Freel</div>
      <div class="contact-line">
        <span>+34 681 503 427</span>
        <svg class="contact-icon" viewBox="0 0 24 24" aria-hidden="true"><path d="M7 2c1 0 2 3 2 4s-2 2-2 3c1 3 3 5 6 6 1 0 2-2 3-2s4 1 4 2-2 4-4 4C9 19 3 12 3 6c0-2 3-4 4-4z" fill="#fff"/></svg>
      </div>
      <div class="contact-line">
        <span>+44 771 4052 368</span>
        <svg class="contact-icon" viewBox="0 0 24 24" aria-hidden="true"><path d="M7 2c1 0 2 3 2 4s-2 2-2 3c1 3 3 5 6 6 1 0 2-2 3-2s4 1 4 2-2 4-4 4C9 19 3 12 3 6c0-2 3-4 4-4z" fill="#fff"/></svg>
      </div>
      <div class="contact-line">
        <span>tobias@morlanex.example</span>
        <svg class="contact-icon" viewBox="0 0 24 24" aria-hidden="true"><rect x="2" y="5" width="20" height="14" rx="1" fill="#fff"/><path d="M3 6l9 7 9-7" fill="none" stroke="#2a8fe0" stroke-width="1.6"/></svg>
      </div>
      <div class="contact-line">
        <span>@Morlanex</span>
        <svg class="contact-icon" viewBox="0 0 24 24" aria-hidden="true"><circle cx="12" cy="12" r="10" fill="#e6eef4"/></svg>
      </div>
    </div>

    <div class="website">www.morlanex.example</div>
  </div>
</body>
</html>
```